Lorena Vex Wigs " Styling Foam"

I need a label created for my product . The bottle size is 50ml so it must be designed to fit that size bottle. I will post my logo and examples of my bottle size. I want the label design to be simple and cute. ill also add pictures of my website, so you can get ideas from there. The bottle is white so I want the main colors to be white and pink. All colors on the label must match my logo. I love glitter as well.

I know for sure I want my logo big, and I want "Styling Foam'',
then under styling foam I would like " Medium Hold" in a different front. be very creative.

Then under that I would like it to say " No Alcohol , Saulfate or Paraben

please make sure on the label in the front it has "NET: 7.0 oz / 200g" so people know what size it is.

I would like a glitter border on the label.

I also want the back of the label to have directions.

And ingredients list too . Very small not too big at all.

Target Market(s)

My target market is woman of all ages .. but mainly woman from ages 26-65

Industry/Entity Type

Hair And Beauty

Font styles to use
Serif
Sans Serif
Decorative
Script

Colors
e667a6
eda3c7
f9d9e8
e34297

Requirements
Must have
• The project must match the colors of my logo, it must have a nice pretty glitter border . It must be simple and clean . But still stylish ! I don’t want everything after my logo to be in the same font . Have fun with this design, be creative. My logo and “ Styling Foam” must be the two centerpiece!
Nice to have
• It will be nice to have different fonts! And nice to have all the colors that match my logo
Must be expensive looking !!
Very eye catching!
Should not have
• Do not add colors that my logo doesn’t have !!!!
I don’t want it to look too plain and boring ! I want it to be classy and expensive looking !

```html
<!DOCTYPE html>
<html lang="en">
<head>
<meta charset="utf-8">
<title>Lorena Vex Wigs – Styling Foam Labels</title>
<link href="https://fonts.googleapis.com/css2?family=Permanent+Marker&family=Oswald:wght@500;600&family=Lilita+One&family=Roboto:wght@400;700&family=Playfair+Display:wght@700&display=swap" rel="stylesheet">
<style>
  :root {
    --backdrop: #6d80a8;
    --pink-deep: #e34297;
    --pink-mid: #e667a6;
    --pink-soft: #eda3c7;
    --pink-pale: #f9d9e8;
    --white: #ffffff;
    --ink: #222222;
  }
  * { margin: 0; padding: 0; box-sizing: border-box; }
  html, body { width: 1200px; height: 975px; overflow: hidden; }
  body { background: var(--backdrop); position: relative; font-family: "Roboto", Arial, sans-serif; }

  .label { position: absolute; top: 285px; width: 244px; height: 550px; overflow: hidden; }
  .label--classic { left: 117px; background: var(--pink-deep); }
  .label--clean { left: 480px; background: var(--white); }
  .label--waves { left: 857px; background: var(--pink-deep); }

  .block { position: absolute; left: 0; width: 100%; }
  .brand { position: absolute; left: 0; width: 100%; text-align: center;
    font-family: "Playfair Display", Georgia, serif; font-weight: 700; font-size: 25px; line-height: 1.05; }
  .brand--light { color: var(--white); }
  .brand--pink { color: var(--pink-deep); }

  .product { position: absolute; left: 0; width: 100%; text-align: center; line-height: 1.02; }
  .product--brush { font-family: "Permanent Marker", cursive; font-size: 38px; }
  .product--bold { font-family: "Lilita One", sans-serif; font-size: 40px; color: var(--white); }

  .hold { position: absolute; font-family: "Oswald", Impact, sans-serif; font-weight: 600; color: var(--ink);
    font-size: 46px; line-height: 1; text-align: right; right: 22px; }
  .hold--band { left: 0; right: 0; text-align: center; color: var(--white); font-size: 29px; font-weight: 500; }

  .claims { position: absolute; right: 22px; text-align: right; font-size: 13px; line-height: 1.3; color: var(--ink); }
  .net { position: absolute; font-size: 12px; font-weight: 700; }
  .net--pill { right: 22px; background: var(--ink); color: var(--white); border-radius: 9px; padding: 2px 9px; }
  .net--plain { right: 22px; color: var(--white); }
  .net--dark { right: 22px; color: var(--ink); }
  .rule { position: absolute; right: 22px; width: 136px; height: 2px; background: var(--ink); }

  .icon-row { position: absolute; left: 0; width: 100%; display: flex; justify-content: center; gap: 14px; }
  .icon { width: 36px; height: 36px; }
</style>
</head>
<body>

<!-- Label: classic -->
<section class="label label--classic">
  <div class="brand brand--light" style="top:115px;">Lorena Vex<br>Wigs</div>
  <div class="block" role="img" aria-label="Soft pink wave pattern with circles" style="top:278px;height:272px;background:linear-gradient(170deg,var(--pink-soft) 0%,var(--pink-pale) 45%,var(--white) 100%);"></div>
  <div class="product product--brush" style="top:198px;color:var(--white);">STYLING<br>FOAM</div>
  <div class="hold" style="top:360px;">MEDIUM<br>HOLD</div>
  <div class="rule" style="top:483px;"></div>
  <div class="claims" style="top:490px;">No Alcohol<br>Saulfate/Paraben</div>
  <div class="net net--pill" style="top:528px;">NET: 7.0 oz / 200g</div>
</section>

<!-- Label: clean -->
<section class="label label--clean">
  <div class="brand brand--pink" style="top:108px;">Lorena Vex<br>Wigs</div>
  <div class="product product--brush" style="top:228px;color:var(--pink-deep);">STYLING<br>FOAM</div>
  <div class="block" style="top:362px;height:58px;background:var(--pink-deep);">
    <div class="hold hold--band" style="top:10px;">MEDIUM HOLD</div>
  </div>
  <div class="block" role="img" aria-label="Pink zigzag pattern" style="top:420px;height:130px;background:linear-gradient(180deg,var(--pink-mid),var(--pink-deep));"></div>
  <div class="icon-row" style="top:445px;">
    <svg class="icon" viewBox="0 0 36 36" aria-hidden="true"><circle cx="18" cy="18" r="16" fill="none" stroke="var(--white)" stroke-width="2"/><line x1="7" y1="29" x2="29" y2="7" stroke="var(--white)" stroke-width="2"/></svg>
    <svg class="icon" viewBox="0 0 36 36" aria-hidden="true"><circle cx="18" cy="18" r="16" fill="none" stroke="var(--white)" stroke-width="2"/><line x1="7" y1="29" x2="29" y2="7" stroke="var(--white)" stroke-width="2"/></svg>
  </div>
  <div class="net net--plain" style="top:527px;">NET: 7.0 oz / 200g</div>
</section>

<!-- Label: waves -->
<section class="label label--waves">
  <div class="block" role="img" aria-label="Soft pink wave pattern with circles" style="top:0;height:165px;background:linear-gradient(165deg,var(--pink-pale) 0%,var(--pink-soft) 70%,var(--pink-mid) 100%);"></div>
  <div class="brand brand--light" style="top:185px;">Lorena Vex<br>Wigs</div>
  <div class="product product--bold" style="top:288px;">STYLING<br>FOAM</div>
  <div class="block" role="img" aria-label="Soft pink wave pattern with circles" style="top:395px;height:155px;background:linear-gradient(170deg,var(--pink-mid) 0%,var(--pink-soft) 40%,var(--pink-pale) 100%);"></div>
  <div class="hold" style="top:380px;right:18px;">MEDIUM<br>HOLD</div>
  <div class="claims" style="top:490px;right:18px;">No Alcohol<br>Saulfate/Paraben</div>
  <div class="net net--dark" style="top:528px;right:18px;">NET: 7.0 oz / 200g</div>
</section>

</body>
</html>
```